Design KICKASS business card and stationary

Update 1: Use Velimor_Logo_rotated *ONLY* ( updated! )
Update 2: Add linkedin address

Consulting company is in need of some really cool stationary and business card. BE CREATIVE
I need a design of our new business cards and stationary, basicly the complete set in 1 consistent design.

colors: blue on white, white on blue, add black, grey or orange

I leave the design up to the experts! GOOD LUCK!!!
Looking forward to your work!

The details for the business card should contain the usual:

Name: Daan Holloway
Role: Project Manager

e-mail: [url removed, login to view]@[url removed, login to view]
mobile: +31698765432
linkedin: [url removed, login to view]
Office address: lindelaan 47, 1000ZK Amsterdam
www: [url removed, login to view]

The details for the stationairy should contain:

Logo

Name: Velimor
Tel: 020 87654321
Email: info@[url removed, login to view]
KvK-nummer: 87654321

```html
<!DOCTYPE html>
<html lang="en">
<head>
<meta charset="utf-8">
<title>Velimor — Business Card</title>
<link href="https://fonts.googleapis.com/css2?family=Montserrat:wght@700&family=Questrial&display=swap" rel="stylesheet">
<style>
  :root {
    --page: #e6e7e9;
    --card-light: #ececed;
    --brand-blue: #1f73b7;
    --deep-blue: #1b66ab;
    --cyan: #29a3cf;
    --ink: #1d1d1f;
    --dark-soft: #3a3a3d;
    --white: #ffffff;
  }
  * { margin: 0; padding: 0; box-sizing: border-box; }
  html, body {
    width: 1200px; height: 900px; overflow: hidden;
    background: var(--page);
    font-family: "Questrial", sans-serif;
  }
  .sheet {
    width: 1200px; height: 900px;
    display: flex; flex-direction: column;
    align-items: center; justify-content: center; gap: 40px;
  }
  .card {
    width: 700px; height: 400px; display: block;
    box-shadow: 0 10px 28px rgba(0,0,0,0.18);
  }
  .logo-name { font-family: "Questrial", sans-serif; font-size: 44px; fill: var(--brand-blue); }
  .holder-name { font-family: "Montserrat", sans-serif; font-weight: 700; font-size: 32px; fill: var(--ink); }
  .holder-role { font-family: "Questrial", sans-serif; font-size: 19px; fill: var(--brand-blue); }
  .contact-line { font-family: "Questrial", sans-serif; font-size: 15px; fill: var(--white); }
  .web-address { font-family: "Questrial", sans-serif; font-size: 18px; fill: var(--white); }
</style>
</head>
<body>
<main class="sheet">

  <svg class="card card-back" viewBox="0 0 700 400" aria-label="Card back">
    <defs>
      <linearGradient id="backShade" x1="0" y1="0" x2="1" y2="1">
        <stop offset="0" stop-color="#3b3b3e"/>
        <stop offset="1" stop-color="#232325"/>
      </linearGradient>
    </defs>
    <rect class="back-base" width="700" height="400" fill="url(#backShade)"/>
    <path class="back-swoosh" d="M0,95 C150,90 250,180 330,270 C390,335 470,380 540,400 L0,400 Z" fill="var(--dark-soft)"/>
    <path class="back-band-edge" d="M300,270 C380,330 520,360 700,320 L700,400 L560,400 C470,380 390,335 300,270 Z" fill="#1a1a1c"/>
    <path class="back-band" d="M330,285 C420,340 560,360 700,335 L700,400 L560,400 C480,380 400,340 330,285 Z" fill="var(--brand-blue)"/>
    <g class="brand-mark">
      <circle cx="236" cy="70" r="18" fill="var(--brand-blue)"/>
      <text class="logo-name" x="266" y="86">Velimor</text>
    </g>
    <text class="web-address" x="520" y="372">www.velimor.com</text>
  </svg>

  <svg class="card card-front" viewBox="0 0 700 400" aria-label="Card front">
    <rect class="front-base" width="700" height="400" fill="var(--card-light)"/>
    <path class="front-rule" d="M0,106 C200,102 280,198 340,260 C420,328 560,358 700,388" fill="none" stroke="var(--ink)" stroke-width="4"/>
    <path class="front-panel" d="M0,116 C200,112 280,208 340,270 C420,338 560,368 700,398 L700,400 L0,400 Z" fill="var(--brand-blue)"/>
    <path class="front-wave" d="M340,270 C420,338 560,368 700,398 L700,400 L560,400 C470,372 400,325 340,270 Z" fill="var(--cyan)"/>
    <path class="front-panel-depth" d="M0,305 C140,340 300,380 440,400 L0,400 Z" fill="var(--deep-blue)"/>

    <g class="brand-mark">
      <circle cx="46" cy="54" r="18" fill="var(--brand-blue)"/>
      <text class="logo-name" x="76" y="70">Velimor</text>
    </g>

    <g class="holder">
      <text class="holder-name" x="660" y="212" text-anchor="end">Daan Holloway</text>
      <text class="holder-role" x="630" y="240" text-anchor="end">Project Manager</text>
    </g>

    <g class="contact-list">
      <g class="contact-phone">
        <path d="M36,186 c2,-3 5,-3 6,-1 l2,3 c1,2 0,3 -1,4 c1,3 3,5 6,6 c1,-1 2,-2 4,-1 l3,2 c2,1 2,4 -1,6 c-8,3 -22,-11 -19,-19 z" fill="var(--white)"/>
        <text class="contact-line" x="66" y="200">+31698765432</text>
      </g>
      <g class="contact-web">
        <circle cx="45" cy="225" r="8" fill="none" stroke="var(--white)" stroke-width="1.6"/>
        <path d="M37,225 h16 M45,217 c-5,5 -5,11 0,16 M45,217 c5,5 5,11 0,16" fill="none" stroke="var(--white)" stroke-width="1.2"/>
        <text class="contact-line" x="66" y="230">www.velimor.com</text>
      </g>
      <g class="contact-mail">
        <rect x="36" y="248" width="18" height="13" rx="1.5" fill="none" stroke="var(--white)" stroke-width="1.6"/>
        <path d="M36,249 l9,7 l9,-7" fill="none" stroke="var(--white)" stroke-width="1.6"/>
        <text class="contact-line" x="66" y="260">daan.holloway@velimor.com</text>
      </g>
      <g class="contact-address">
        <path d="M35,286 l10,-9 l10,9 M38,284 v9 h14 v-9" fill="none" stroke="var(--white)" stroke-width="1.6"/>
        <text class="contact-line" x="66" y="290">lindelaan 47, 1000ZK Amsterdam</text>
      </g>
    </g>
  </svg>

</main>
</body>
</html>
```